I am writing a book called "SMILING OPENS EVERY DOOR "

I NEED A BOOK COVER FOR MY BOOK" SMILING OPENS EVERY DOOR"
So who is at the doorstep? " ( this in smaller font)

"Smiling Opens Every Door " will need to designed to eventually be a logo , banner and business card
COLOURS MAINLY ORANGE AND WHITE (with accents bright colour )

THE BOOK IS MY LAUGHTER JOURNEY AS A PERFORMER AND ADVENTURE INDIA LEARNING ABOUT LAUGHTER YOGA WHICH I WILL BE TEACHING

I do not want photos on the front cover ..
The look could be modern and eye-catching
I have also just been to India to learn Laughing Yoga with Dr Tobin Verhaal

Thank-you so much everyone for your brilliant designs . i am overwhelmed with your talent . i hope to work with you all again soon ! Marnie  

Target Market(s)

"Adults based in western speaking countries aged 25 to 60 that want to learn to laugh more
Also this book will be sold at my conference workshops

Industry/Entity Type

Business

Requirements
Must have
• ORANGE AND WHITE
CAN HAVE AQUA , HOT PINK , LIME GREEN, YELLOW ACCENTS

THESE WILL BE DIFFERENT AREAS WILL COVERING IN MY BOOK
EG LAUGHTER NAD BREAT CANCER ( PINK)
LAUGHTER NAD DEPRESSION ( BLUE)
LAUGHTER AND KIDS ( YELLOW)

NO Photos on front cover
Should not have
• No photos

```html
<!DOCTYPE html>
<html lang="en">
<head>
<meta charset="utf-8">
<title>Smiling Opens Every Door — Marnie Halwick</title>
<link rel="stylesheet" href="https://fonts.googleapis.com/css2?family=Jost:wght@400;500&display=swap">
<style>
  :root {
    --paper: #ffffff;
    --spine-outer: #a2b1ae;
    --spine-inner: #3d4a4a;
    --aqua: #7ff5d8;
    --orange: #ff6000;
    --orange-mid: #ff8a3d;
    --orange-soft: #fbc9a8;
    --rule: #e65100;
    --rule-light: #f07a2a;
  }
  * { margin: 0; padding: 0; box-sizing: border-box; }
  html, body { width: 900px; height: 1200px; overflow: hidden; background: var(--paper); }
  .cover {
    position: relative; width: 900px; height: 1200px; background: var(--paper);
    font-family: "Jost", "Futura", sans-serif; color: var(--paper);
  }
  .author-band {
    position: absolute; left: 42px; top: 0; width: 220px; height: 1200px;
    background: var(--spine-outer);
  }
  .author-strip {
    position: absolute; left: 26px; top: 0; width: 168px; height: 1200px;
    background: var(--spine-inner);
  }
  .author-name {
    position: absolute; left: 0; width: 168px; display: flex; flex-direction: column;
    align-items: center; color: var(--aqua); font-weight: 500; font-size: 64px; line-height: 78px;
  }
  .author-first { top: 62px; }
  .author-last { top: 618px; }
  .title-panel {
    position: absolute; left: 314px; top: 0; width: 518px; height: 1200px;
    background: linear-gradient(to bottom,
      var(--orange) 0, var(--orange) 280px, var(--orange-mid) 440px,
      var(--orange-soft) 560px, #fde7da 760px, var(--paper) 1000px);
  }
  .title { position: absolute; top: 14px; left: 0; width: 518px; font-weight: 500; }
  .line { display: flex; justify-content: space-between; font-size: 84px; line-height: 78px; height: 80px; }
  .line .gap { width: 22px; }
  .rule { position: absolute; left: 0; width: 518px; height: 2px; background: var(--rule); }
  .rule.light { background: var(--rule-light); }
  .subtitle {
    position: absolute; left: 0; top: 312px; width: 518px; font-weight: 500;
  }
  .subtitle-top { display: flex; justify-content: space-between; font-size: 48px; line-height: 60px; }
  .subtitle-bottom { display: flex; justify-content: space-between; font-size: 40px; line-height: 48px; margin-top: 26px; }
  .emblem-area {
    position: absolute; left: 0; top: 490px; width: 518px; height: 520px;
    background: radial-gradient(ellipse at 50% 55%, rgba(255,255,255,0.95) 0, rgba(255,255,255,0.6) 45%, rgba(255,255,255,0) 72%);
  }
</style>
</head>
<body>
<main class="cover">
  <aside class="author-band">
    <div class="author-strip">
      <div class="author-name author-first"><span>M</span><span>A</span><span>R</span><span>N</span><span>I</span><span>E</span></div>
      <div class="author-name author-last"><span>H</span><span>A</span><span>L</span><span>W</span><span>I</span><span>C</span><span>K</span></div>
    </div>
  </aside>

  <section class="title-panel">
    <h1 class="title" aria-label="Smiling Opens Every Door">
      <div class="line"><span>S</span><span>M</span><span>I</span><span>L</span><span>I</span><span>N</span><span>G</span></div>
      <div class="line"><span>O</span><span>P</span><span>E</span><span>N</span><span>S</span></div>
      <div class="line"><span>E</span><span>V</span><span>E</span><span>R</span><span>Y</span><span class="gap"></span><span>D</span><span>O</span><span>O</span><span>R</span></div>
    </h1>

    <div class="rule" style="top:268px"></div>
    <div class="rule" style="top:287px"></div>

    <h2 class="subtitle" aria-label="So who is at the doorstep?">
      <div class="subtitle-top"><span>SO</span><span>WHO</span><span>IS</span><span>AT</span><span>THE</span></div>
      <div class="subtitle-bottom"><span>D</span><span>O</span><span>O</span><span>R</span><span>S</span><span>T</span><span>E</span><span>P</span><span>?</span></div>
    </h2>

    <div class="rule light" style="top:461px"></div>
    <div class="rule light" style="top:480px"></div>

    <div class="emblem-area" role="img" aria-label="Large white Om symbol with a soft glow"></div>
  </section>
</main>
</body>
</html>
```